Fenwick Nutrition Therapy needs a business card design

I need a business card design for my private practice. Green is my favorite color. I would like the back of the card to include an area for future appointment dates and time. I provide nutrition therapy to individuals, groups and families. I work a lot with adolescents and women who have eating disorders, but also work with athletes.
Updates

Reason: I received several new designs and would like to take some time reviewing them.

Target Market(s)

I am working primarily with women, but also men (mostly athletes). I work with a lot of runners. I work with people who are 14-60's.

Industry/Entity Type

Nutrition

Font styles to use
Serif
Sans Serif

Colors
9bcb3c
acd037

Requirements
Nice to have
• I would love to have 'Fenwick' incorporated into the design since it is my last name. If possible, I'd love to have an actual moon if it looks professional.

A picture of food could also be on the card if it is simple, but not sure how it would look with Fenwick. I am open to ideas for both Fenwick and a picture of a food item.

Other font style are fine as long as they are easy to read.

```html
<!DOCTYPE html>
<html lang="en">
<head>
<meta charset="utf-8">
<title>Fenwick Nutrition Therapy – Business Card</title>
<link rel="stylesheet" href="https://fonts.googleapis.com/css2?family=Cormorant:wght@500&family=Lato:wght@400&display=swap">
<style>
  :root {
    --backdrop: #ebebeb;
    --card-white: #ffffff;
    --card-mint: #e7f2c6;
    --brand-green: #9bcb3c;
    --rule-green: #acd037;
    --ink: #141414;
    --ink-soft: #2a2a2a;
  }
  * { margin: 0; padding: 0; box-sizing: border-box; }
  html, body {
    width: 1200px; height: 861px; overflow: hidden;
    background: var(--backdrop);
  }
  .sheet {
    width: 1200px; height: 861px;
    display: flex; align-items: center; justify-content: center; gap: 40px;
  }
  .card {
    width: 540px; height: 309px;
    position: relative;
    box-shadow: 0 2px 6px rgba(0,0,0,0.12);
  }
  .card--front { background: var(--card-white); }
  .card--back { background: var(--card-mint); }

  .practice-name {
    position: absolute;
    font-family: "Lato", sans-serif;
    font-weight: 400;
    color: var(--ink);
    white-space: nowrap;
  }
  .card--front .practice-name { left: 40px; top: 40px; font-size: 26px; }
  .card--back .practice-name { left: 30px; top: 26px; font-size: 18px; }

  .accent-band {
    position: absolute; left: 40px; top: 86px;
    width: 60px; height: 3px; background: var(--brand-green);
  }

  .contact {
    position: absolute; left: 40px; top: 112px;
    font-family: "Lato", sans-serif; color: var(--ink-soft);
  }
  .contact__name { font-size: 16px; color: var(--ink); letter-spacing: 0.3px; }
  .contact__creds { font-size: 11px; margin-top: 3px; }
  .contact__address { font-size: 12px; line-height: 1.35; margin-top: 6px; }
  .contact__phone { font-size: 19px; color: var(--ink); margin-top: 14px; }
  .contact__fax { font-size: 12px; margin-top: 2px; }
  .contact__email {
    position: absolute; right: 30px; bottom: 26px;
    font-family: "Lato", sans-serif; font-size: 13px; color: var(--ink-soft);
  }

  .field-label {
    position: absolute;
    font-family: "Cormorant", serif; font-weight: 500;
    font-size: 16px; color: var(--ink); letter-spacing: 1px;
  }
  .field-label--date { left: 30px; top: 72px; }
  .field-label--time { left: 250px; top: 72px; }
  .field-label--notes { left: 250px; top: 130px; }
  .rule {
    position: absolute; height: 1px; background: var(--rule-green);
  }
</style>
</head>
<body>
<main class="sheet">
  <section class="card card--front" aria-label="Card front">
    <h1 class="practice-name">Fenwick Nutrition Therapy</h1>
    <div class="accent-band"></div>
    <div class="contact">
      <p class="contact__name">DANA WHITLOW FENWICK</p>
      <p class="contact__creds">MS, RDN, LDN</p>
      <p class="contact__address">4417 Maple Hollow Lane<br>Brookfield, TN 37900</p>
      <p class="contact__phone">Phone: 555-014-2276</p>
      <p class="contact__fax">Fax: 555-014-2290</p>
    </div>
    <p class="contact__email">dfenwick@mailhaven.net</p>
  </section>

  <section class="card card--back" aria-label="Card back, appointment reminder">
    <h2 class="practice-name">Fenwick Nutrition Therapy</h2>

    <span class="field-label field-label--date">DATE</span>
    <div class="rule" style="left:30px; top:112px; width:190px;"></div>

    <span class="field-label field-label--time">TIME</span>
    <div class="rule" style="left:250px; top:112px; width:260px;"></div>

    <span class="field-label field-label--notes">NOTES</span>
    <div class="rule" style="left:250px; top:170px; width:260px;"></div>
    <div class="rule" style="left:250px; top:200px; width:260px;"></div>
    <div class="rule" style="left:250px; top:230px; width:260px;"></div>
    <div class="rule" style="left:250px; top:260px; width:260px;"></div>
    <div class="rule" style="left:250px; top:288px; width:260px;"></div>
  </section>
</main>
</body>
</html>
```